529 aim Higher

Redesigning this front and back business card flyer and keeping the info but making it look better.

This is all about using the info and logo on the business card design and creating a better layout using any of the following and more.

Changing the background color or imagine, chaining the placement of content, resizing content.

Target Market(s)

Targeting people that have been injured on one side and people that have been giving a DUI on the other.

Contact Information for Business Card

We are looking to keep the info but make it look a fee cleaner and less cluttered

Font styles to use
Sans Serif

Requirements
Must have
• Must have the same info but a better layout.
Nice to have
• better background colors or image or layout. different fonts or same font all design options that will make it look professional and clean.

```html
<!DOCTYPE html>
<html lang="en">
<head>
<meta charset="utf-8">
<title>529 aim Higher – Business Cards</title>
<link href="https://fonts.googleapis.com/css2?family=Bowlby+One&family=Open+Sans:wght@400;600&display=swap" rel="stylesheet">
<style>
  :root {
    --stage: #2b2b2d;
    --card: #ffffff;
    --ink: #232323;
    --red: #d3202b;
    --panel: #1f1d1e;
    --muted: #f1f1f1;
  }
  * { box-sizing: border-box; margin: 0; padding: 0; }
  html, body { width: 1200px; height: 900px; overflow: hidden; }
  body {
    background: var(--stage);
    font-family: "Open Sans", Arial, sans-serif;
    color: var(--ink);
    display: flex;
    flex-direction: column;
    align-items: center;
    justify-content: center;
    gap: 36px;
  }
  .card {
    width: 720px;
    height: 400px;
    background: var(--card);
    border-radius: 16px;
    overflow: hidden;
    display: flex;
  }
  .card__body {
    flex: 1;
    padding: 24px 28px 20px 34px;
    display: flex;
    flex-direction: column;
  }
  .card__brand {
    width: 168px;
    background: var(--panel);
    border-left: 7px solid var(--red);
    display: flex;
    align-items: center;
    justify-content: center;
  }
  .brand-name {
    writing-mode: vertical-rl;
    font-family: "Bowlby One", Impact, sans-serif;
    font-size: 40px;
    line-height: 1;
    color: #ffffff;
    white-space: nowrap;
    letter-spacing: 1px;
  }
  .heavy { font-family: "Bowlby One", Impact, sans-serif; line-height: 1.05; }
  .call { color: var(--red); }
  .web { color: var(--ink); }
  .red { color: var(--red); }

  .bullets { list-style: none; }
  .bullets li {
    position: relative;
    padding-left: 24px;
  }
  .bullets li::before {
    content: "";
    position: absolute;
    left: 2px;
    top: 0.42em;
    width: 12px;
    height: 12px;
    border: 2.5px solid var(--red);
    border-radius: 50%;
  }
  .bullets li::after {
    content: "";
    position: absolute;
    left: 3px;
    top: calc(0.42em + 5px);
    width: 10px;
    height: 2.5px;
    background: var(--red);
    transform: rotate(-45deg);
  }

  /* Injury card */
  .injury .call { font-size: 34px; }
  .injury .web { font-size: 24px; margin-top: 2px; }
  .injury .headline { font-size: 22px; margin-top: 12px; }
  .injury .bullets { font-size: 16px; line-height: 1.35; margin-top: 4px; }
  .photos { display: flex; gap: 14px; margin-top: 12px; }
  .photo { width: 150px; height: 100px; }
  .photo--crash { background: linear-gradient(135deg, #3a1014, #6b6e78 60%, #1b1b22); }
  .photo--crutch { background: linear-gradient(180deg, #b9b6b1, #8f8b86); }
  .photo--window { background: linear-gradient(90deg, #151414, #5d5a55 55%, #1c1b1a); }
  .injury .tagline { font-size: 18px; color: var(--red); margin-top: auto; }

  /* DUI card */
  .dui .call { font-size: 42px; }
  .dui .web { font-size: 30px; margin-top: 2px; }
  .dui .headline { font-size: 36px; margin-top: 10px; }
  .dui .question {
    font-size: 15px;
    padding-bottom: 5px;
    border-bottom: 2px solid var(--red);
    margin-top: 2px;
  }
  .dui .bullets { font-size: 17px; line-height: 1.3; margin-top: 8px; }
  .dui .small { font-size: 12px; }
</style>
</head>
<body>

  <article class="card injury">
    <div class="card__body">
      <p class="heavy call">CALL 529-246-4437</p>
      <p class="heavy web">www.529aimhigher.com</p>
      <p class="heavy headline red">If You've Been Injured DON'T SETTLE</p>
      <ul class="bullets">
        <li>for an inexperienced lawyer!</li>
        <li>for less than you deserve!</li>
        <li>for paying massive medical bills!</li>
        <li>for a life of pain and debt!</li>
      </ul>
      <div class="photos">
        <div class="photo photo--crash" role="img" aria-label="Photo of a damaged car at a night-time crash scene"></div>
        <div class="photo photo--crutch" role="img" aria-label="Photo of an injured leg in a walking boot with crutches"></div>
        <div class="photo photo--window" role="img" aria-label="Photo of a person in a wheelchair by a window in silhouette"></div>
      </div>
      <p class="heavy tagline">We fight for you, so you can focus on getting better</p>
    </div>
    <div class="card__brand"><span class="brand-name">529 aim Higher</span></div>
  </article>

  <article class="card dui">
    <div class="card__body">
      <p class="heavy call">CALL 529-246-4437</p>
      <p class="heavy web">www.529aimhigher.com</p>
      <p class="heavy headline red">DON'T SETTLE FOR A DUI</p>
      <p class="heavy question">WHAT SHOULD I DO IF I GET PULLED OVER FOR DUI?</p>
      <ul class="bullets">
        <li>Pull over in a calm, normal manner</li>
        <li>Be polite at all times</li>
        <li>Do not admit to drinking</li>
        <li>Do not submit to any field sobriety tests</li>
        <li>Do not submit to taking a chemical test <span class="small">(breath, blood, or urine)</span></li>
        <li>Do not make any statement after being arrested, especially when placed in the police cruiser</li>
      </ul>
    </div>
    <div class="card__brand"><span class="brand-name">529 aim Higher</span></div>
  </article>

</body>
</html>
```